Need new Spot UV Business Card design

We are looking for a new business card design incorporating Spot UV in black & white options / versions. See examples files and Mireno Castel Design logo.
You can see our website at www.mirenocastel-example.ca. We want something classy but yet modern. We are open to black or black and/or white on white with the spot uv. We are open to portrait or landscape. Size should be standard 3.5" x 2". The front of the card should focus on the logo and name "Mireno Castel" only. Fonts used should be "Open sans" or "PT Sans".

Target Market(s)

Mid to high end

Industry/Entity Type

Business

Contact Information for Business Card

Tobin Ferrash
555.304.8172
tobin@mirenocastel-example.ca
www.mirenocastel-example.ca
4917 Alderwick Blvd. W Suite 308
Mississauga, ON K7R 2B9

Requirements
Must have
• Name & Logo

```html
<!DOCTYPE html>
<html lang="en">
<head>
<meta charset="utf-8">
<title>Mireno Castel Design – Business Card</title>
<link rel="stylesheet" href="https://fonts.googleapis.com/css2?family=Open+Sans:wght@400;700&display=swap">
<style>
  :root {
    --backdrop: #1b1b1c;
    --card: #2b2b2c;
    --card-edge: #333334;
    --pattern-a: #262627;
    --pattern-b: #303031;
    --silver: #a9a9ab;
    --silver-soft: #8c8c8e;
  }
  * { margin: 0; padding: 0; box-sizing: border-box; }
  html, body {
    width: 1200px;
    height: 974px;
    overflow: hidden;
    background: var(--backdrop);
    font-family: "Open Sans", Arial, sans-serif;
  }
  .sheet {
    width: 1200px;
    height: 974px;
    display: flex;
    flex-direction: column;
    align-items: center;
    justify-content: center;
    gap: 44px;
  }
  .card {
    position: relative;
    width: 700px;
    height: 400px;
    background: var(--card);
    border: 1px solid var(--card-edge);
    overflow: hidden;
  }
  .card-front .uv-pattern {
    position: absolute;
    inset: 0;
    background: linear-gradient(135deg, var(--pattern-b), var(--pattern-a) 55%, var(--pattern-b));
  }
  .front-brand {
    position: absolute;
    inset: 0;
    display: flex;
    align-items: center;
    justify-content: center;
    gap: 22px;
  }
  .brand-square {
    width: 78px;
    height: 78px;
    border: 4px solid var(--silver);
    background: var(--card);
  }
  .front-name {
    font-size: 44px;
    font-weight: 400;
    letter-spacing: 3px;
    color: var(--silver);
    text-transform: uppercase;
  }
  .card-back {
    display: flex;
    flex-direction: column;
    align-items: center;
    text-align: center;
  }
  .back-brand {
    margin-top: 92px;
    display: flex;
    align-items: center;
    gap: 10px;
  }
  .back-brand .brand-square {
    width: 26px;
    height: 26px;
    border-width: 2px;
  }
  .back-name {
    font-size: 32px;
    font-weight: 400;
    letter-spacing: 2px;
    color: var(--silver-soft);
    text-transform: uppercase;
  }
  .person {
    margin-top: 88px;
    font-size: 19px;
    font-weight: 700;
    letter-spacing: 1px;
    color: var(--silver-soft);
    text-transform: uppercase;
  }
  .contact {
    margin-top: 14px;
    font-size: 15px;
    line-height: 1.6;
    color: var(--silver-soft);
  }
  .contact .sep { margin: 0 8px; }
</style>
</head>
<body>
<main class="sheet">
  <section class="card card-front">
    <div class="uv-pattern" role="img" aria-label="Spot UV gloss pattern of repeating outlined squares across the card"></div>
    <div class="front-brand">
      <span class="brand-square"></span>
      <span class="front-name">Mireno Castel</span>
    </div>
  </section>

  <section class="card card-back">
    <div class="back-brand">
      <span class="brand-square"></span>
      <span class="back-name">Mireno Castel</span>
    </div>
    <p class="person">Tobin Ferrash</p>
    <p class="contact">
      555.304.8172<span class="sep">|</span>tobin@mirenocastel-example.ca<span class="sep">|</span>www.mirenocastel-example.ca<br>
      4917 Alderwick Blvd. W Suite 308, Mississauga, ON K7R 2B9
    </p>
  </section>
</main>
</body>
</html>
```